Create branded design templates/backgrounds for social media based on UK property investing company

I'd like Instagram, Facebook and Linkedin backgrounds/templates to add text to, based on my logo design and business of UK holiday let investing. Ideally I'd have some base designs for me to approve, then engage with the winning designer further to create about 50 different templates. I looking for a mixture of templates with the logo and using logo colours, others of internal holiday let photos including logos and a few of my photo imposed on the front of them.
Updates

Slow in providing feedback

Target Market(s)

Middle aged adults

Industry/Entity Type

Holiday let properties

Requirements
Must have
• a distinct brand look that can be replicated

```html
<!DOCTYPE html>
<html lang="en">
<head>
<meta charset="UTF-8">
<title>Northgate Stays – Social Templates</title>
<link href="https://fonts.googleapis.com/css2?family=Plus+Jakarta+Sans:wght@400;500;600;700;800&family=Allura&display=swap" rel="stylesheet">
<style>
  :root {
    --brand-blue: #0a7fd8;
    --brand-blue-deep: #0560c4;
    --brand-blue-soft: #3fa0e6;
    --accent-yellow: #f5dc2a;
    --ink: #141414;
    --white: #ffffff;
    --page: #ffffff;
  }
  * { margin: 0; padding: 0; box-sizing: border-box; }
  html, body { width: 1200px; height: 582px; overflow: hidden; background: var(--page); }
  body { position: relative; font-family: "Plus Jakarta Sans", Arial, sans-serif; }

  .post {
    position: absolute;
    top: 117px;
    width: 349px;
    height: 349px;
    overflow: hidden;
    box-shadow: 0 10px 18px rgba(0,0,0,.28);
  }
  .post--growth { left: 53px; }
  .post--portrait { left: 425px; background: var(--white); }
  .post--quote { left: 799px; }

  .scene-fill { position: absolute; inset: 0; }
  .post--growth .scene-fill {
    background: linear-gradient(120deg, var(--brand-blue-deep) 0%, var(--brand-blue) 45%, #2f7fc9 75%, #1f66b4 100%);
  }
  .post--quote .scene-fill {
    background: linear-gradient(160deg, var(--brand-blue-soft) 0%, var(--brand-blue) 55%, #0b86d6 100%);
  }
  .post--portrait .scene-fill {
    background: linear-gradient(180deg, var(--white) 0%, var(--white) 40%, #cfe3f3 62%, #3d8fd6 80%, var(--brand-blue-deep) 100%);
  }
  .portrait-photo {
    position: absolute;
    left: 12px; top: 20px;
    width: 245px; height: 329px;
    border-radius: 110px 110px 0 0;
    background: linear-gradient(180deg, #e9c6ad 0%, #dcb39a 45%, #6b6d66 62%, #595b55 100%);
  }

  .brand {
    position: absolute;
    top: 22px; right: 18px;
    display: flex; align-items: center; gap: 6px;
    font-weight: 600; font-size: 13px; letter-spacing: .2px;
    color: var(--white);
  }
  .brand__mark { width: 12px; height: 12px; background: currentColor; }
  .post--portrait .brand { color: var(--brand-blue-deep); }

  .zigzag { position: absolute; inset: 0; }

  .headline {
    position: absolute; left: 34px; top: 88px;
    color: var(--white); font-weight: 500;
    font-size: 35px; line-height: 33px; letter-spacing: -.3px;
  }
  .headline .highlight { color: var(--accent-yellow); font-weight: 700; }
  .supporting {
    position: absolute; left: 35px; top: 228px;
    color: var(--accent-yellow); font-size: 7.5px; line-height: 9.5px; letter-spacing: -.2px;
  }

  .signature { position: absolute; color: var(--white); text-align: right; }
  .signature__name { font-family: "Allura", cursive; font-size: 36px; line-height: 30px; }
  .signature__role { font-size: 7px; font-weight: 600; margin-top: -2px; }
  .post--growth .signature { left: 34px; top: 280px; }
  .post--quote .signature { left: 116px; top: 228px; }

  .signature-band {
    position: absolute; left: 205px; top: 192px; width: 144px; height: 56px;
    background: var(--white);
  }
  .post--portrait .signature { right: 12px; top: 203px; color: var(--ink); }

  .statement {
    position: absolute; right: 18px; top: 80px;
    text-align: right; color: var(--ink);
    font-size: 25px; line-height: 28px; letter-spacing: -1.2px; font-weight: 400;
  }
  .statement strong { font-weight: 700; }

  .quote {
    position: absolute; left: 0; right: 0; top: 118px;
    text-align: center; color: var(--white);
    font-size: 30.5px; line-height: 32px; font-weight: 600; letter-spacing: -.6px;
  }
  .quote strong { font-weight: 800; }
  .quote .mark { color: var(--accent-yellow); font-size: 22px; vertical-align: 8px; }
</style>
</head>
<body>

  <section class="post post--growth">
    <div class="scene-fill" role="img" aria-label="Brick terraced house photograph under a blue colour overlay"></div>
    <div class="brand"><span class="brand__mark"></span>Northgate Stays</div>
    <h1 class="headline">Make<br><span class="highlight">evolution</span> in<br>your<br>business</h1>
    <p class="supporting">Lorem ipsum dolor sit amet,<br>consectetur adipiscing elit.</p>
    <div class="signature">
      <div class="signature__name">Your Name</div>
      <div class="signature__role">Business Owner</div>
    </div>
    <svg class="zigzag" viewBox="0 0 349 349" aria-hidden="true">
      <polyline points="380,265 255,302 322,343 280,370" fill="none" stroke="var(--accent-yellow)" stroke-width="30" stroke-linejoin="miter"/>
    </svg>
  </section>

  <section class="post post--portrait">
    <div class="scene-fill" role="img" aria-label="Suburban houses and street fading from white into blue"></div>
    <div class="portrait-photo" role="img" aria-label="Portrait photograph of the business owner"></div>
    <div class="brand"><span class="brand__mark"></span>Northgate Stays</div>
    <p class="statement">Always provide<br>the <strong>best service</strong><br>in everything</p>
    <div class="signature-band"></div>
    <div class="signature">
      <div class="signature__name">Your Name</div>
      <div class="signature__role">Business Owner</div>
    </div>
  </section>

  <section class="post post--quote">
    <div class="scene-fill" role="img" aria-label="Detached brick house photograph under a blue colour overlay"></div>
    <div class="brand"><span class="brand__mark"></span>Northgate Stays</div>
    <p class="quote"><span class="mark">“</span>Focus on looking<br>to <strong>the future</strong><br>to get best result<span class="mark">”</span></p>
    <div class="signature">
      <div class="signature__name">Your Name</div>
      <div class="signature__role">Business Owner</div>
    </div>
    <svg class="zigzag" viewBox="0 0 349 349" aria-hidden="true">
      <polyline points="-20,278 100,300 30,345 60,370" fill="none" stroke="var(--accent-yellow)" stroke-width="32" stroke-linejoin="miter"/>
      <polyline points="250,370 335,305 330,370" fill="none" stroke="var(--accent-yellow)" stroke-width="30" stroke-linejoin="miter"/>
    </svg>
  </section>

</body>
</html>
```